Creative Businesss Card desgin!

Create a business card for our business Gleam window cleaning!
We are open to creative ideas as long as it maintains a professional image.

Target Market(s)

Small Commercial window cleaning clients including car dealerships, strata manager, cafe

Industry/Entity Type

Window Cleaning

Contact Information for Business Card

Daniel Prescott
General Manager
Gleam Window Cleaning

daniel@gleamservices.com.au
pane-care-southbank.com.au
Ph: 1800 GET GLEAM
Mob: 0437 582 061

Colors
fbed22
0392cd

Requirements
Should not have
• Stock window cleaning/ squeegee graphics

```html
<!DOCTYPE html>
<html lang="en">
<head>
<meta charset="utf-8">
<title>Gleam Window Cleaning – Business Card</title>
<link rel="stylesheet" href="https://fonts.googleapis.com/css2?family=Work+Sans:wght@400;500;700;800&display=swap">
<style>
  :root {
    --backdrop: #141414;
    --card: #1e1e1e;
    --card-edge: #262626;
    --brand-yellow: #f4ee1c;
    --text-light: #f2f2f2;
    --emboss-grey: #8c8c8c;
    --url-grey: #5a5a5a;
  }
  * { box-sizing: border-box; margin: 0; padding: 0; }
  html, body {
    width: 1200px;
    height: 900px;
    overflow: hidden;
    background: var(--backdrop);
    font-family: "Work Sans", sans-serif;
  }
  .stage {
    position: relative;
    width: 1200px;
    height: 900px;
  }
  .card {
    position: absolute;
    left: 240px;
    width: 720px;
    height: 410px;
    background: linear-gradient(135deg, var(--card) 0%, var(--card-edge) 100%);
    box-shadow: 0 18px 40px rgba(0,0,0,0.55);
  }
  .card--front { top: 25px; }
  .card--back { top: 465px; }

  /* Front */
  .front-wordmark {
    position: absolute;
    left: 0; right: 0;
    top: 120px;
    text-align: center;
    color: var(--emboss-grey);
    font-weight: 800;
    line-height: 1;
  }
  .front-wordmark .wordmark-name { display: block; font-size: 92px; letter-spacing: 2px; }
  .front-wordmark .wordmark-tag { display: block; font-size: 30px; margin-top: 6px; letter-spacing: 1px; }
  .front-url {
    position: absolute;
    left: 0; right: 0;
    top: 318px;
    text-align: center;
    color: var(--url-grey);
    font-size: 17px;
    letter-spacing: 0.5px;
  }

  /* Back */
  .back-wordmark {
    position: absolute;
    left: 52px;
    top: 140px;
    color: var(--brand-yellow);
    font-weight: 800;
    line-height: 1;
  }
  .back-wordmark .wordmark-name { display: block; font-size: 76px; letter-spacing: 1px; }
  .back-wordmark .wordmark-tag { display: block; font-size: 25px; margin-top: 6px; }
  .divider {
    position: absolute;
    left: 352px;
    top: 105px;
    width: 2px;
    height: 170px;
    background: var(--brand-yellow);
  }
  .contact {
    position: absolute;
    left: 390px;
    top: 112px;
    color: var(--text-light);
  }
  .contact-name {
    color: var(--brand-yellow);
    font-weight: 700;
    font-size: 27px;
    letter-spacing: 2.5px;
    text-transform: uppercase;
  }
  .contact-role {
    font-size: 17px;
    letter-spacing: 1px;
    margin-top: 2px;
    margin-bottom: 22px;
  }
  .contact-list { list-style: none; }
  .contact-list li {
    display: flex;
    align-items: center;
    gap: 10px;
    font-size: 17px;
    letter-spacing: 0.6px;
    line-height: 24px;
  }
  .contact-icon {
    width: 12px;
    height: 12px;
    flex: none;
    stroke: var(--brand-yellow);
    fill: none;
    stroke-width: 1.5;
  }
</style>
</head>
<body>
<main class="stage">

  <section class="card card--front" aria-label="Card front">
    <div class="front-wordmark">
      <span class="wordmark-name">GLEAM</span>
      <span class="wordmark-tag">WINDOW CLEANING</span>
    </div>
    <p class="front-url">pane-care-southbank.com.au</p>
  </section>

  <section class="card card--back" aria-label="Card back">
    <div class="back-wordmark">
      <span class="wordmark-name">GLEAM</span>
      <span class="wordmark-tag">WINDOW CLEANING</span>
    </div>
    <div class="divider"></div>
    <div class="contact">
      <h1 class="contact-name">Daniel Prescott</h1>
      <p class="contact-role">General Manager</p>
      <ul class="contact-list">
        <li>
          <svg class="contact-icon" viewBox="0 0 12 12" aria-hidden="true"><path d="M2.5 1.5l2 2.2-1 1.2a6 6 0 0 0 3.6 3.6l1.2-1 2.2 2-1.3 1.3C5.5 10.5 1.5 6.5 1.2 2.8z"/></svg>
          1800 GET GLEAM
        </li>
        <li>
          <svg class="contact-icon" viewBox="0 0 12 12" aria-hidden="true"><rect x="3" y="1" width="6" height="10" rx="1"/><line x1="5.2" y1="9" x2="6.8" y2="9"/></svg>
          0437 582 061
        </li>
        <li>
          <svg class="contact-icon" viewBox="0 0 12 12" aria-hidden="true"><rect x="1" y="2.5" width="10" height="7"/><path d="M1 2.5l5 4 5-4"/></svg>
          daniel@gleamservices.com.au
        </li>
        <li>
          <svg class="contact-icon" viewBox="0 0 12 12" aria-hidden="true"><circle cx="6" cy="6" r="5"/><ellipse cx="6" cy="6" rx="2.2" ry="5"/><line x1="1" y1="6" x2="11" y2="6"/></svg>
          pane-care-southbank.com.au
        </li>
      </ul>
    </div>
  </section>

</main>
</body>
</html>
```